LUMEN PI Planning Web App - Lean Agile at Scale - Distributed Big Room Planning Web & Touchscr...

We are the provider of the boardweave app http://boardweave-demo.example which currently is a desktop application. We are now working to bring all the features to a web-app but we don’t have a catchy design yet. The boardweave app is a visual collaboration tool for globally distributed teams and organization. Imagine a wall with lots of sticky notes on a flipchart hanging there – that’s basically our app just in a digital format. In general we want a light, modern, state of the art look and feel. Please take colorblind people into consideration when designing it.We are specifically looking for the following two design parts:- Design of the board structure- Sticky note designRequirements for the board structure- 16:9 ratio fixed- The board can be structured in 2 to 12 iterations + Risk Area and Objectives. Most common is 5 iterations + Risk Area and Objectives. Please go with the most common one but have in the back of your head that it needs to be compatible with 14 sections. Just for your imagination: in real life each of these areas on the board is one flip chart page.- Team Name: Somewhere on the board has to be the team name. It has to be easy to find and read.- In the iteration fields the user can set a velocity. That’s a simple numbers field. The load is calculated automatically and is just a number displayed on the board. There is an automatic visual indicator which should show with green or red colors if the teams are still in the plan. How this is brought to the attention is up to you.- Objectives & Stretch Objectives: The area with the Objectives is a list with text and a prioritization number attached to it. BV on the sketch stands for Business Value.Sticky Note design descriptionThe Sticky Note represents a physical sticky note or post-it note. When the user sees it he should instantly understand it as a sticky note and so for intuitively know what to do with it.Unselected sticky noteIf the sticky note is not selected it should be a simple sticky note sitting on the board.Following you find the things visible when the sticky note is not selected:- The sticky notes have a squared form factor- There is the text which is on the sticky note- In the upper right corner is a small sticky ID. Something like e.g. RT-4253.- Somewhere on the sticky note is also a number which should be easy to read. The numbers range from nothing over 0.5, 1, 2, 3, 5, 8, 13, 20, 40 up to 100.- Somewhere on the sticky needs to be a permanent text label. Not bigger than the rest of the text on the sticky note but easy to read.Selected sticky noteIf the user clicks on the sticky note once the following information needs to be displayed and he needs to be able to do the things listed and described below:- The sticky notes have a squared form factor- The user can write text on it- He can select different colors. These colors need to have a label so he knows what the function of these colors are.- By clicking a button he can add a flag to the sticky note- He can open a selection to choose the following number displayed on the sticky: 0.5, 1, 2, 3, 5, 8, 13, 20, 40, 100.- There is a delete sticky button. Place it where it makes sense from an intuitive stand point.- If he clicks the delete button, a short dialog appears on the sticky note: “Are you sure you want to delete this sticky note permanently? (It might delete an issue in your ALM tool)” He can confirm that by pressing “Delete” or “Cancel”.- In the upper right corner is a small sticky ID. Something like e.g. RT-4253.- Somewhere on or next to the sticky note needs to be a “sticky mirror” button as well as a “sticky move” button. Beside an optional icon for “mirror” and “move” there needs to be a naming tag so that everyone understands it right away.- It’s up to you to decide what’s the most intuitive way for the user.For better understanding also take a look at the rough sketch attached.

Font styles to use
Sans Serif

Requirements
Must have
• Color blind mode for different colored sticky notes

```html
<!DOCTYPE html>
<html lang="en">
<head>
<meta charset="utf-8">
<title>LUMEN PI Planning Board – boardweave</title>
<link rel="stylesheet" href="https://fonts.googleapis.com/css2?family=Source+Sans+3:wght@300;400&display=swap">
<style>
  :root{
    --canvas:#ffffff;
    --panel:#f2f2f2;
    --panel-border:#9a9a9a;
    --hanger:#6b6b6b;
    --header:#4d4d4d;
    --tab:#e6e6e6;
    --label:#b3b3b3;
    --field:#e6e6e6;
    --text:#4d4d4d;
    --muted:#9a9a9a;
    --footer:#808080;
    --footer-end:#4d4d4d;

    --slate:#6e929e;
    --orange:#f15a24;
    --purple:#4b2c7c;
    --olive:#5f5f36;
    --red:#ed1c24;
    --amber:#fbb03b;
    --pink:#ed1e79;
    --lime:#8cc63f;
    --orchid:#cc66cc;
    --cyan:#29abe2;
    --navy:#2e3192;
    --forest:#006837;
  }
  *{box-sizing:border-box;margin:0;padding:0}
  html,body{width:1200px;height:675px;overflow:hidden;background:var(--canvas)}
  body{font-family:"Source Sans 3",sans-serif;font-weight:300;color:var(--text);position:relative}

  .section{position:absolute;background:var(--panel);border:1px solid var(--panel-border)}
  .section::before{content:"";position:absolute;top:-7px;left:49px;width:121px;height:6px;background:var(--hanger)}

  .iteration{top:54px;width:220px;height:265px}
  .iteration__header{height:19px;background:var(--header);position:relative}
  .team-name{position:absolute;left:17px;top:0;width:75px;height:19px;background:var(--tab);
    font-size:9px;line-height:19px;text-align:center;color:var(--text)}
  .iteration__title{position:absolute;left:16px;top:31px;font-size:9px;color:var(--muted)}
  .metric{position:absolute;left:136px;display:flex;height:14px}
  .metric--velocity{top:28px}
  .metric--load{top:44px}
  .metric__label{width:39px;background:var(--label);color:#fff;font-size:8px;line-height:14px;text-align:center}
  .metric__value{width:34px;background:var(--field)}

  .sticky-grid{position:absolute;display:grid}
  .iteration .sticky-grid{left:15px;top:66px;grid-template-columns:repeat(3,59px);grid-auto-rows:59px;column-gap:9px;row-gap:7px}

  .sticky{position:relative;background:var(--c);border-bottom-right-radius:10px;
    box-shadow:1px 2px 2px rgba(0,0,0,.25);overflow:hidden}
  .sticky::after{content:"";position:absolute;right:0;bottom:0;width:12px;height:14px;
    background:rgba(0,0,0,.32);border-top-left-radius:100% 100%}
  .sticky__bar{height:9px;background:rgba(255,255,255,.25);display:flex;align-items:center;
    justify-content:space-between;padding:0 2px 0 3px}
  .sticky__label{font-size:4px;color:rgba(255,255,255,.85)}
  .sticky__tools{display:flex;gap:1px}
  .sticky__tools span{width:5px;height:5px;border:1px solid rgba(255,255,255,.85)}
  .sticky__meta{display:flex;align-items:center;height:9px;padding:0 2px 0 4px;gap:3px}
  .sticky__menu{width:6px;height:4px;border-top:1px solid #fff;border-bottom:1px solid #fff;position:relative}
  .sticky__menu::after{content:"";position:absolute;left:0;right:0;top:1px;border-top:1px solid #fff}
  .sticky__points{margin-left:auto;font-size:4px;color:rgba(255,255,255,.85)}
  .sticky__id{font-size:4px;color:rgba(255,255,255,.9);background:rgba(0,0,0,.2);padding:0 2px;line-height:6px}

  .sticky--slate{--c:var(--slate)} .sticky--orange{--c:var(--orange)} .sticky--purple{--c:var(--purple)}
  .sticky--olive{--c:var(--olive)} .sticky--red{--c:var(--red)} .sticky--amber{--c:var(--amber)}
  .sticky--pink{--c:var(--pink)} .sticky--lime{--c:var(--lime)} .sticky--orchid{--c:var(--orchid)}
  .sticky--cyan{--c:var(--cyan)} .sticky--navy{--c:var(--navy)} .sticky--forest{--c:var(--forest)}

  .area{top:349px;width:220px;height:264px}
  .area__footer{position:absolute;left:0;right:0;bottom:0;height:18px;background:var(--footer)}
  .area__footer::before,.area__footer::after{content:"";position:absolute;top:0;width:17px;height:18px;background:var(--footer-end)}
  .area__footer::before{left:0}.area__footer::after{right:0}
  .area__title{position:absolute;font-size:9px;text-transform:uppercase}

  .objectives .area__title{left:22px;top:24px}
  .objectives__group{position:absolute;left:54px;font-size:8.5px}
  .objectives__group--business{top:48px}
  .objectives__list{list-style:none;margin-top:6px;font-size:8px;line-height:12px}
  .objectives__group--stretch{top:136px}

  .risks .area__title{left:12px;top:27px}
  .risks .sticky-grid{left:21px;top:67px;grid-template-columns:repeat(4,40px);grid-auto-rows:40px;column-gap:6px;row-gap:5px}
  .risks .sticky__bar{height:7px}
  .risks .sticky__meta{height:7px}
  .risks .sticky::after{width:9px;height:10px}
</style>
</head>
<body>
<main class="board" aria-label="LUMEN PI planning board">

  <!-- iteration sections -->
  <section class="section iteration" style="left:22px">
    <header class="iteration__header"><h2 class="team-name">Team Name</h2></header>
    <p class="iteration__title">Iteration 1</p>
    <div class="metric metric--velocity"><span class="metric__label">Velocity</span><span class="metric__value"></span></div>
    <div class="metric metric--load"><span class="metric__label">Load</span><span class="metric__value"></span></div>
    <div class="sticky-grid">
      <div class="sticky sticky--slate"><div class="sticky__bar"><span class="sticky__label">StickyName</span><span class="sticky__tools"><span></span><span></span><span></span></span></div><div class="sticky__meta"><span class="sticky__menu"></span><span class="sticky__points">0.5</span><span class="sticky__id">RT-4253</span></div></div>
      <div class="sticky sticky--orange"><div class="sticky__bar"><span class="sticky__label">StickyName</span><span class="sticky__tools"><span></span><span></span><span></span></span></div><div class="sticky__meta"><span class="sticky__menu"></span><span class="sticky__points">0.5</span><span class="sticky__id">RT-4253</span></div></div>
      <div class="sticky sticky--purple"><div class="sticky__bar"><span class="sticky__label">StickyName</span><span class="sticky__tools"><span></span><span></span><span></span></span></div><div class="sticky__meta"><span class="sticky__menu"></span><span class="sticky__points">0.5</span><span class="sticky__id">RT-4253</span></div></div>
      <div class="sticky sticky--olive"><div class="sticky__bar"><span class="sticky__label">StickyName</span><span class="sticky__tools"><span></span><span></span><span></span></span></div><div class="sticky__meta"><span class="sticky__menu"></span><span class="sticky__points">0.5</span><span class="sticky__id">RT-4253</span></div></div>
      <div class="sticky sticky--red"><div class="sticky__bar"><span class="sticky__label">StickyName</span><span class="sticky__tools"><span></span><span></span><span></span></span></div><div class="sticky__meta"><span class="sticky__menu"></span><span class="sticky__points">0.5</span><span class="sticky__id">RT-4253</span></div></div>
      <div class="sticky sticky--amber"><div class="sticky__bar"><span class="sticky__label">StickyName</span><span class="sticky__tools"><span></span><span></span><span></span></span></div><div class="sticky__meta"><span class="sticky__menu"></span><span class="sticky__points">0.5</span><span class="sticky__id">RT-4253</span></div></div>
      <div class="sticky sticky--pink"><div class="sticky__bar"><span class="sticky__label">StickyName</span><span class="sticky__tools"><span></span><span></span><span></span></span></div><div class="sticky__meta"><span class="sticky__menu"></span><span class="sticky__points">0.5</span><span class="sticky__id">RT-4253</span></div></div>
      <div class="sticky sticky--lime"><div class="sticky__bar"><span class="sticky__label">StickyName</span><span class="sticky__tools"><span></span><span></span><span></span></span></div><div class="sticky__meta"><span class="sticky__menu"></span><span class="sticky__points">0.5</span><span class="sticky__id">RT-4253</span></div></div>
      <div class="sticky sticky--orchid"><div class="sticky__bar"><span class="sticky__label">StickyName</span><span class="sticky__tools"><span></span><span></span><span></span></span></div><div class="sticky__meta"><span class="sticky__menu"></span><span class="sticky__points">0.5</span><span class="sticky__id">RT-4253</span></div></div>
    </div>
  </section>

  <section class="section iteration" style="left:256px">
    <header class="iteration__header"><h2 class="team-name">Team Name</h2></header>
    <p class="iteration__title">Iteration 1</p>
    <div class="metric metric--velocity"><span class="metric__label">Velocity</span><span class="metric__value"></span></div>
    <div class="metric metric--load"><span class="metric__label">Load</span><span class="metric__value"></span></div>
    <div class="sticky-grid">
      <div class="sticky sticky--slate"><div class="sticky__bar"><span class="sticky__label">StickyName</span><span class="sticky__tools"><span></span><span></span><span></span></span></div><div class="sticky__meta"><span class="sticky__menu"></span><span class="sticky__points">0.5</span><span class="sticky__id">RT-4253</span></div></div>
      <div class="sticky sticky--orange"><div class="sticky__bar"><span class="sticky__label">StickyName</span><span class="sticky__tools"><span></span><span></span><span></span></span></div><div class="sticky__meta"><span class="sticky__menu"></span><span class="sticky__points">0.5</span><span class="sticky__id">RT-4253</span></div></div>
      <div class="sticky sticky--purple"><div class="sticky__bar"><span class="sticky__label">StickyName</span><span class="sticky__tools"><span></span><span></span><span></span></span></div><div class="sticky__meta"><span class="sticky__menu"></span><span class="sticky__points">0.5</span><span class="sticky__id">RT-4253</span></div></div>
      <div class="sticky sticky--olive"><div class="sticky__bar"><span class="sticky__label">StickyName</span><span class="sticky__tools"><span></span><span></span><span></span></span></div><div class="sticky__meta"><span class="sticky__menu"></span><span class="sticky__points">0.5</span><span class="sticky__id">RT-4253</span></div></div>
      <div class="sticky sticky--red"><div class="sticky__bar"><span class="sticky__label">StickyName</span><span class="sticky__tools"><span></span><span></span><span></span></span></div><div class="sticky__meta"><span class="sticky__menu"></span><span class="sticky__points">0.5</span><span class="sticky__id">RT-4253</span></div></div>
      <div class="sticky sticky--amber"><div class="sticky__bar"><span class="sticky__label">StickyName</span><span class="sticky__tools"><span></span><span></span><span></span></span></div><div class="sticky__meta"><span class="sticky__menu"></span><span class="sticky__points">0.5</span><span class="sticky__id">RT-4253</span></div></div>
      <div class="sticky sticky--pink"><div class="sticky__bar"><span class="sticky__label">StickyName</span><span class="sticky__tools"><span></span><span></span><span></span></span></div><div class="sticky__meta"><span class="sticky__menu"></span><span class="sticky__points">0.5</span><span class="sticky__id">RT-4253</span></div></div>
      <div class="sticky sticky--lime"><div class="sticky__bar"><span class="sticky__label">StickyName</span><span class="sticky__tools"><span></span><span></span><span></span></span></div><div class="sticky__meta"><span class="sticky__menu"></span><span class="sticky__points">0.5</span><span class="sticky__id">RT-4253</span></div></div>
      <div class="sticky sticky--orchid"><div class="sticky__bar"><span class="sticky__label">StickyName</span><span class="sticky__tools"><span></span><span></span><span></span></span></div><div class="sticky__meta"><span class="sticky__menu"></span><span class="sticky__points">0.5</span><span class="sticky__id">RT-4253</span></div></div>
    </div>
  </section>

  <section class="section iteration" style="left:489px">
    <header class="iteration__header"><h2 class="team-name">Team Name</h2></header>
    <p class="iteration__title">Iteration 1</p>
    <div class="metric metric--velocity"><span class="metric__label">Velocity</span><span class="metric__value"></span></div>
    <div class="metric metric--load"><span class="metric__label">Load</span><span class="metric__value"></span></div>
    <div class="sticky-grid">
      <div class="sticky sticky--slate"><div class="sticky__bar"><span class="sticky__label">StickyName</span><span class="sticky__tools"><span></span><span></span><span></span></span></div><div class="sticky__meta"><span class="sticky__menu"></span><span class="sticky__points">0.5</span><span class="sticky__id">RT-4253</span></div></div>
      <div class="sticky sticky--orange"><div class="sticky__bar"><span class="sticky__label">StickyName</span><span class="sticky__tools"><span></span><span></span><span></span></span></div><div class="sticky__meta"><span class="sticky__menu"></span><span class="sticky__points">0.5</span><span class="sticky__id">RT-4253</span></div></div>
      <div class="sticky sticky--purple"><div class="sticky__bar"><span class="sticky__label">StickyName</span><span class="sticky__tools"><span></span><span></span><span></span></span></div><div class="sticky__meta"><span class="sticky__menu"></span><span class="sticky__points">0.5</span><span class="sticky__id">RT-4253</span></div></div>
      <div class="sticky sticky--olive"><div class="sticky__bar"><span class="sticky__label">StickyName</span><span class="sticky__tools"><span></span><span></span><span></span></span></div><div class="sticky__meta"><span class="sticky__menu"></span><span class="sticky__points">0.5</span><span class="sticky__id">RT-4253</span></div></div>
      <div class="sticky sticky--red"><div class="sticky__bar"><span class="sticky__label">StickyName</span><span class="sticky__tools"><span></span><span></span><span></span></span></div><div class="sticky__meta"><span class="sticky__menu"></span><span class="sticky__points">0.5</span><span class="sticky__id">RT-4253</span></div></div>
      <div class="sticky sticky--amber"><div class="sticky__bar"><span class="sticky__label">StickyName</span><span class="sticky__tools"><span></span><span></span><span></span></span></div><div class="sticky__meta"><span class="sticky__menu"></span><span class="sticky__points">0.5</span><span class="sticky__id">RT-4253</span></div></div>
      <div class="sticky sticky--pink"><div class="sticky__bar"><span class="sticky__label">StickyName</span><span class="sticky__tools"><span></span><span></span><span></span></span></div><div class="sticky__meta"><span class="sticky__menu"></span><span class="sticky__points">0.5</span><span class="sticky__id">RT-4253</span></div></div>
      <div class="sticky sticky--lime"><div class="sticky__bar"><span class="sticky__label">StickyName</span><span class="sticky__tools"><span></span><span></span><span></span></span></div><div class="sticky__meta"><span class="sticky__menu"></span><span class="sticky__points">0.5</span><span class="sticky__id">RT-4253</span></div></div>
      <div class="sticky sticky--orchid"><div class="sticky__bar"><span class="sticky__label">StickyName</span><span class="sticky__tools"><span></span><span></span><span></span></span></div><div class="sticky__meta"><span class="sticky__menu"></span><span class="sticky__points">0.5</span><span class="sticky__id">RT-4253</span></div></div>
    </div>
  </section>

  <section class="section iteration" style="left:722px">
    <header class="iteration__header"><h2 class="team-name">Team Name</h2></header>
    <p class="iteration__title">Iteration 1</p>
    <div class="metric metric--velocity"><span class="metric__label">Velocity</span><span class="metric__value"></span></div>
    <div class="metric metric--load"><span class="metric__label">Load</span><span class="metric__value"></span></div>
    <div class="sticky-grid">
      <div class="sticky sticky--slate"><div class="sticky__bar"><span class="sticky__label">StickyName</span><span class="sticky__tools"><span></span><span></span><span></span></span></div><div class="sticky__meta"><span class="sticky__menu"></span><span class="sticky__points">0.5</span><span class="sticky__id">RT-4253</span></div></div>
      <div class="sticky sticky--orange"><div class="sticky__bar"><span class="sticky__label">StickyName</span><span class="sticky__tools"><span></span><span></span><span></span></span></div><div class="sticky__meta"><span class="sticky__menu"></span><span class="sticky__points">0.5</span><span class="sticky__id">RT-4253</span></div></div>
      <div class="sticky sticky--purple"><div class="sticky__bar"><span class="sticky__label">StickyName</span><span class="sticky__tools"><span></span><span></span><span></span></span></div><div class="sticky__meta"><span class="sticky__menu"></span><span class="sticky__points">0.5</span><span class="sticky__id">RT-4253</span></div></div>
      <div class="sticky sticky--olive"><div class="sticky__bar"><span class="sticky__label">StickyName</span><span class="sticky__tools"><span></span><span></span><span></span></span></div><div class="sticky__meta"><span class="sticky__menu"></span><span class="sticky__points">0.5</span><span class="sticky__id">RT-4253</span></div></div>
      <div class="sticky sticky--red"><div class="sticky__bar"><span class="sticky__label">StickyName</span><span class="sticky__tools"><span></span><span></span><span></span></span></div><div class="sticky__meta"><span class="sticky__menu"></span><span class="sticky__points">0.5</span><span class="sticky__id">RT-4253</span></div></div>
      <div class="sticky sticky--amber"><div class="sticky__bar"><span class="sticky__label">StickyName</span><span class="sticky__tools"><span></span><span></span><span></span></span></div><div class="sticky__meta"><span class="sticky__menu"></span><span class="sticky__points">0.5</span><span class="sticky__id">RT-4253</span></div></div>
      <div class="sticky sticky--pink"><div class="sticky__bar"><span class="sticky__label">StickyName</span><span class="sticky__tools"><span></span><span></span><span></span></span></div><div class="sticky__meta"><span class="sticky__menu"></span><span class="sticky__points">0.5</span><span class="sticky__id">RT-4253</span></div></div>
      <div class="sticky sticky--lime"><div class="sticky__bar"><span class="sticky__label">StickyName</span><span class="sticky__tools"><span></span><span></span><span></span></span></div><div class="sticky__meta"><span class="sticky__menu"></span><span class="sticky__points">0.5</span><span class="sticky__id">RT-4253</span></div></div>
      <div class="sticky sticky--orchid"><div class="sticky__bar"><span class="sticky__label">StickyName</span><span class="sticky__tools"><span></span><span></span><span></span></span></div><div class="sticky__meta"><span class="sticky__menu"></span><span class="sticky__points">0.5</span><span class="sticky__id">RT-4253</span></div></div>
    </div>
  </section>

  <section class="section iteration" style="left:955px">
    <header class="iteration__header"><h2 class="team-name">Team Name</h2></header>
    <p class="iteration__title">Iteration 1</p>
    <div class="metric metric--velocity"><span class="metric__label">Velocity</span><span class="metric__value"></span></div>
    <div class="metric metric--load"><span class="metric__label">Load</span><span class="metric__value"></span></div>
    <div class="sticky-grid">
      <div class="sticky sticky--slate"><div class="sticky__bar"><span class="sticky__label">StickyName</span><span class="sticky__tools"><span></span><span></span><span></span></span></div><div class="sticky__meta"><span class="sticky__menu"></span><span class="sticky__points">0.5</span><span class="sticky__id">RT-4253</span></div></div>
      <div class="sticky sticky--orange"><div class="sticky__bar"><span class="sticky__label">StickyName</span><span class="sticky__tools"><span></span><span></span><span></span></span></div><div class="sticky__meta"><span class="sticky__menu"></span><span class="sticky__points">0.5</span><span class="sticky__id">RT-4253</span></div></div>
      <div class="sticky sticky--purple"><div class="sticky__bar"><span class="sticky__label">StickyName</span><span class="sticky__tools"><span></span><span></span><span></span></span></div><div class="sticky__meta"><span class="sticky__menu"></span><span class="sticky__points">0.5</span><span class="sticky__id">RT-4253</span></div></div>
      <div class="sticky sticky--olive"><div class="sticky__bar"><span class="sticky__label">StickyName</span><span class="sticky__tools"><span></span><span></span><span></span></span></div><div class="sticky__meta"><span class="sticky__menu"></span><span class="sticky__points">0.5</span><span class="sticky__id">RT-4253</span></div></div>
      <div class="sticky sticky--red"><div class="sticky__bar"><span class="sticky__label">StickyName</span><span class="sticky__tools"><span></span><span></span><span></span></span></div><div class="sticky__meta"><span class="sticky__menu"></span><span class="sticky__points">0.5</span><span class="sticky__id">RT-4253</span></div></div>
      <div class="sticky sticky--amber"><div class="sticky__bar"><span class="sticky__label">StickyName</span><span class="sticky__tools"><span></span><span></span><span></span></span></div><div class="sticky__meta"><span class="sticky__menu"></span><span class="sticky__points">0.5</span><span class="sticky__id">RT-4253</span></div></div>
      <div class="sticky sticky--pink"><div class="sticky__bar"><span class="sticky__label">StickyName</span><span class="sticky__tools"><span></span><span></span><span></span></span></div><div class="sticky__meta"><span class="sticky__menu"></span><span class="sticky__points">0.5</span><span class="sticky__id">RT-4253</span></div></div>
      <div class="sticky sticky--lime"><div class="sticky__bar"><span class="sticky__label">StickyName</span><span class="sticky__tools"><span></span><span></span><span></span></span></div><div class="sticky__meta"><span class="sticky__menu"></span><span class="sticky__points">0.5</span><span class="sticky__id">RT-4253</span></div></div>
      <div class="sticky sticky--orchid"><div class="sticky__bar"><span class="sticky__label">StickyName</span><span class="sticky__tools"><span></span><span></span><span></span></span></div><div class="sticky__meta"><span class="sticky__menu"></span><span class="sticky__points">0.5</span><span class="sticky__id">RT-4253</span></div></div>
    </div>
  </section>

  <!-- objectives -->
  <section class="section area objectives" style="left:22px">
    <h2 class="area__title">Objectives</h2>
    <div class="objectives__group objectives__group--business">
      <h3 style="font-weight:300;font-size:8.5px">Business Values</h3>
      <ol class="objectives__list"><li>1.</li><li>2.</li><li>3.</li><li>4.</li></ol>
    </div>
    <div class="objectives__group objectives__group--stretch">
      <h3 style="font-weight:300;font-size:8.5px">Stretch Objectives</h3>
    </div>
    <div class="area__footer"></div>
  </section>

  <!-- risks -->
  <section class="section area risks" style="left:256px">
    <h2 class="area__title">Risks</h2>
    <div class="sticky-grid">
      <div class="sticky sticky--slate"><div class="sticky__bar"><span class="sticky__label">StickyName</span><span class="sticky__tools"><span></span><span></span></span></div><div class="sticky__meta"><span class="sticky__menu"></span><span class="sticky__points">0.5</span><span class="sticky__id">RT-4253</span></div></div>
      <div class="sticky sticky--orange"><div class="sticky__bar"><span class="sticky__label">StickyName</span><span class="sticky__tools"><span></span><span></span></span></div><div class="sticky__meta"><span class="sticky__menu"></span><span class="sticky__points">0.5</span><span class="sticky__id">RT-4253</span></div></div>
      <div class="sticky sticky--purple"><div class="sticky__bar"><span class="sticky__label">StickyName</span><span class="sticky__tools"><span></span><span></span></span></div><div class="sticky__meta"><span class="sticky__menu"></span><span class="sticky__points">0.5</span><span class="sticky__id">RT-4253</span></div></div>
      <div class="sticky sticky--cyan"><div class="sticky__bar"><span class="sticky__label">StickyName</span><span class="sticky__tools"><span></span><span></span></span></div><div class="sticky__meta"><span class="sticky__menu"></span><span class="sticky__points">0.5</span><span class="sticky__id">RT-4253</span></div></div>
      <div class="sticky sticky--olive"><div class="sticky__bar"><span class="sticky__label">StickyName</span><span class="sticky__tools"><span></span><span></span></span></div><div class="sticky__meta"><span class="sticky__menu"></span><span class="sticky__points">0.5</span><span class="sticky__id">RT-4253</span></div></div>
      <div class="sticky sticky--red"><div class="sticky__bar"><span class="sticky__label">StickyName</span><span class="sticky__tools"><span></span><span></span></span></div><div class="sticky__meta"><span class="sticky__menu"></span><span class="sticky__points">0.5</span><span class="sticky__id">RT-4253</span></div></div>
      <div class="sticky sticky--amber"><div class="sticky__bar"><span class="sticky__label">StickyName</span><span class="sticky__tools"><span></span><span></span></span></div><div class="sticky__meta"><span class="sticky__menu"></span><span class="sticky__points">0.5</span><span class="sticky__id">RT-4253</span></div></div>
      <div class="sticky sticky--navy"><div class="sticky__bar"><span class="sticky__label">StickyName</span><span class="sticky__tools"><span></span><span></span></span></div><div class="sticky__meta"><span class="sticky__menu"></span><span class="sticky__points">0.5</span><span class="sticky__id">RT-4253</span></div></div>
      <div class="sticky sticky--pink"><div class="sticky__bar"><span class="sticky__label">StickyName</span><span class="sticky__tools"><span></span><span></span></span></div><div class="sticky__meta"><span class="sticky__menu"></span><span class="sticky__points">0.5</span><span class="sticky__id">RT-4253</span></div></div>
      <div class="sticky sticky--lime"><div class="sticky__bar"><span class="sticky__label">StickyName</span><span class="sticky__tools"><span></span><span></span></span></div><div class="sticky__meta"><span class="sticky__menu"></span><span class="sticky__points">0.5</span><span class="sticky__id">RT-4253</span></div></div>
      <div class="sticky sticky--orchid"><div class="sticky__bar"><span class="sticky__label">StickyName</span><span class="sticky__tools"><span></span><span></span></span></div><div class="sticky__meta"><span class="sticky__menu"></span><span class="sticky__points">0.5</span><span class="sticky__id">RT-4253</span></div></div>
      <div class="sticky sticky--forest"><div class="sticky__bar"><span class="sticky__label">StickyName</span><span class="sticky__tools"><span></span><span></span></span></div><div class="sticky__meta"><span class="sticky__menu"></span><span class="sticky__points">0.5</span><span class="sticky__id">RT-4253</span></div></div>
    </div>
    <div class="area__footer"></div>
  </section>

</main>
</body>
</html>
```